Bricks in the Wall

We need graphics for a 5x7 or 6x9 post card, single sided for a small speech language pathology practice that serves pediatric patients primarily with children on the autism spectrum.

I want a brick wall, with words and phrases written into the bricks. (to follow)
A child standing on top of the wall with hands up in success.
A few incomplete autism puzzles on the ground.
A larger complete autism puzzle in the the child's hand.
The title is: Speech/Language Therapy
The Foundation for Communication Success
Words/phrases to go into the red bricks:
Receptive Language, Expressive Language, Pragmatics, Sensory, cognitive,
social language, autism, articulation, TeleTherapy, auditory processing, screening, evaluation, developmental delay, Goals, family involvement, environmental communication, ASD, Mirror Neurons.

Target Market(s)

Children with speech and language disorders.

Industry/Entity Type

Speech and Language Therapy

Font styles to use
Serif

Requirements
Must have
• Colors, primary and red bricks.
Nice to have
• I want the postcard to have a happy feel to it and a sense of success.
Should not have
• I don't want it cluttered.

```html
<!DOCTYPE html>
<html lang="en">
<head>
<meta charset="utf-8">
<title>Speech/Language Therapy – The Foundation for Communication Success</title>
<link rel="stylesheet" href="https://fonts.googleapis.com/css2?family=Alfa+Slab+One&family=Arvo:wght@700&display=swap">
<style>
  :root {
    --orange: #f39a1c;
    --orange-deep: #e8780f;
    --orange-light: #f7b02c;
    --ground: #d9670e;
    --rust: #d4501c;
    --brick: #c7321f;
    --brick-dark: #a82716;
    --mortar: #efe6da;
    --ink: #232a31;
    --paper: #ffffff;
    --sky-blue: #2f7fd1;
    --sun-yellow: #ffd23a;
    --leaf-green: #3aa655;
  }
  html, body {
    margin: 0;
    padding: 0;
    width: 1200px;
    height: 729px;
    overflow: hidden;
    background: #ffffff;
  }
  .postcard {
    position: relative;
    width: 1200px;
    height: 729px;
    overflow: hidden;
    background: linear-gradient(160deg, var(--orange-light) 0%, var(--orange) 45%, var(--orange-deep) 100%);
    font-family: "Arvo", Georgia, serif;
  }
  .backdrop {
    position: absolute;
    inset: 0;
    width: 1200px;
    height: 729px;
  }
  .title {
    position: absolute;
    right: 56px;
    top: 30px;
    margin: 0;
    text-align: right;
    color: var(--ink);
    font-weight: 400;
  }
  .title-main {
    display: block;
    font-family: "Alfa Slab One", Georgia, serif;
    font-size: 58px;
    line-height: 1.05;
  }
  .title-sub {
    display: block;
    margin-top: 8px;
    font-family: "Alfa Slab One", Georgia, serif;
    font-size: 27px;
    line-height: 1.2;
  }
  .child-figure {
    position: absolute;
    left: 150px;
    top: 88px;
    width: 130px;
    height: 200px;
    border-radius: 60px 60px 10px 10px;
    background: linear-gradient(180deg, var(--sun-yellow) 0%, var(--sky-blue) 100%);
  }
  .wall {
    position: absolute;
    left: 30px;
    top: 288px;
    width: 1140px;
    padding: 6px;
    box-sizing: border-box;
    background: var(--mortar);
    display: flex;
    flex-direction: column;
    gap: 6px;
    box-shadow: 0 6px 10px rgba(0,0,0,0.2);
  }
  .wall-row {
    display: flex;
    gap: 6px;
    height: 64px;
  }
  .wall-row--offset { padding-left: 34px; }
  .wall-row--offset-end { padding-right: 34px; }
  .brick {
    flex: 1 1 auto;
    display: flex;
    align-items: center;
    justify-content: center;
    padding: 0 14px;
    background: linear-gradient(180deg, var(--brick) 0%, var(--brick-dark) 100%);
    color: var(--paper);
    font-family: "Arvo", Georgia, serif;
    font-weight: 700;
    font-size: 19px;
    white-space: nowrap;
  }
  .ground-puzzle {
    position: absolute;
    width: 74px;
    height: 74px;
    border-radius: 8px;
  }
  .ground-puzzle--blue { left: 110px; top: 626px; background: var(--sky-blue); transform: rotate(-12deg); }
  .ground-puzzle--yellow { left: 520px; top: 634px; background: var(--sun-yellow); transform: rotate(9deg); }
  .ground-puzzle--green { left: 960px; top: 624px; background: var(--leaf-green); transform: rotate(-6deg); }
</style>
</head>
<body>
<main class="postcard">
  <svg class="backdrop" viewBox="0 0 1200 729" aria-hidden="true">
    <polygon points="0,592 1200,592 1200,729 0,729" fill="var(--ground)"/>
    <rect x="0" y="592" width="1200" height="10" fill="var(--rust)"/>
  </svg>

  <h1 class="title">
    <span class="title-main">Speech/Language Therapy</span>
    <span class="title-sub">The Foundation for Communication Success</span>
  </h1>

  <div class="child-figure" role="img" aria-label="Happy child standing on top of the wall with arms raised, holding a large completed puzzle"></div>

  <section class="wall" aria-label="Brick wall of therapy topics">
    <div class="wall-row">
      <span class="brick">Receptive Language</span>
      <span class="brick">Expressive Language</span>
      <span class="brick">Pragmatics</span>
      <span class="brick">Sensory</span>
    </div>
    <div class="wall-row wall-row--offset">
      <span class="brick">Cognitive</span>
      <span class="brick">Social Language</span>
      <span class="brick">Autism</span>
      <span class="brick">Articulation</span>
      <span class="brick">TeleTherapy</span>
    </div>
    <div class="wall-row wall-row--offset-end">
      <span class="brick">Auditory Processing</span>
      <span class="brick">Screening</span>
      <span class="brick">Evaluation</span>
      <span class="brick">Developmental Delay</span>
    </div>
    <div class="wall-row">
      <span class="brick">Goals</span>
      <span class="brick">Family Involvement</span>
      <span class="brick">Environmental Communication</span>
      <span class="brick">ASD</span>
      <span class="brick">Mirror Neurons</span>
    </div>
  </section>

  <div class="ground-puzzle ground-puzzle--blue" role="img" aria-label="Incomplete puzzle lying on the ground"></div>
  <div class="ground-puzzle ground-puzzle--yellow" role="img" aria-label="Incomplete puzzle lying on the ground"></div>
  <div class="ground-puzzle ground-puzzle--green" role="img" aria-label="Incomplete puzzle lying on the ground"></div>
</main>
</body>
</html>
```